依頼詳細
東北や北海道の学校等に求人を行います。詳細の条件が示された求人票は別途準備しますので、当社のポイントを明示した、魅力を感じていただけるようなチラシをお願いしたいと思います。ポイントはまとめておりますので、画像やイラスト等も使用して、仕上げていただければありがたいです。また時間がないため、期日は短めでお願いする形となりますが、何卒宜しくお願い申し上げます。
記載項目
別資料参照。
サイズ
A4
ページ数
片面
希望イメージ
シンプル 複雑
単色 カラフル
暗い 明るい
日常 高級
遊び心 厳粛
未来的 伝統的
女性的 男性的
希望する色
黄・オレンジ系、緑系、水色系
①施設HPのQRコードを追加で準備いたしました。こちらも入れていただければと思います。
②法人名を失念しておりました。『株式会社LUMA』となりますので、こちらも追加記載をお願いいたします。
■ 選んだ理由

アニメ調で、学生への訴求効果が高いように感じたこと。またとても目を引くデザインであったこと。

■ 提案者全員のお礼・コメント

非常に多くのご提案をいただきましてありがとうございました。良いものばかりで、ひとつに絞り込むのが非常に困難でした…。また依頼を行わせていただくと思いますが、今後とも宜しくお願い申し上げます。

```html
<!DOCTYPE html>
<html lang="ja">
<head>
<meta charset="UTF-8">
<title>こもれび 採用案内</title>
<link rel="stylesheet" href="https://fonts.googleapis.com/css2?family=M+PLUS+Rounded+1c:wght@400;700;800&family=Zen+Maru+Gothic:wght@500;700;900&display=swap">
<style>
:root{
  --pink:#ef5f9a;
  --pink-deep:#e2457f;
  --pink-pale:#fde6ef;
  --yellow:#fff07a;
  --cream:#fffaf4;
  --ink:#4a3a3f;
  --white:#ffffff;
}
*{margin:0;padding:0;box-sizing:border-box}
html,body{width:846px;height:1200px;overflow:hidden}
body{font-family:"M PLUS Rounded 1c",sans-serif;color:var(--ink);background:var(--cream)}
.flyer{position:relative;width:846px;height:1200px;overflow:hidden;
  background:radial-gradient(circle at 80% 70%,#fff3d8 0,transparent 40%),radial-gradient(circle at 15% 85%,#ffe4ee 0,transparent 40%),var(--cream)}
.top-band{position:absolute;top:0;left:0;width:846px;height:66px;background:var(--pink);
  color:var(--white);font-family:"Zen Maru Gothic",sans-serif;font-weight:900;font-size:36px;
  text-align:center;line-height:66px;letter-spacing:3px}
.hero-photo{position:absolute;top:66px;left:0;width:846px;height:590px;
  background:linear-gradient(160deg,#fffdf8 0%,#fbeee3 40%,#f2d6c2 65%,#fff6ee 100%)}
.wishes{position:absolute;top:110px;right:44px;text-align:right;
  font-family:"Zen Maru Gothic",sans-serif;font-weight:900;font-size:34px;color:var(--pink);line-height:1.75;
  text-shadow:0 0 6px #fff,0 0 6px #fff}
.invite{position:absolute;top:420px;left:40px;font-family:"Zen Maru Gothic",sans-serif;font-weight:900;color:var(--white)}
.invite .lead{font-size:36px;text-shadow:0 0 4px var(--pink-deep),0 0 8px var(--pink-deep)}
.invite .main{display:block;margin-top:10px;font-size:48px;color:var(--pink);background:var(--white);
  padding:4px 20px;border-radius:10px;box-shadow:0 0 0 4px var(--pink)}
.features{position:absolute;top:676px;left:26px;width:794px;display:grid;
  grid-template-columns:repeat(3,1fr);gap:26px 18px}
.feature h2{font-family:"Zen Maru Gothic",sans-serif;font-weight:900;font-size:21px;color:var(--pink);
  text-align:center;border-bottom:3px solid var(--pink);padding-bottom:6px;margin-bottom:8px}
.feature p{font-size:13px;line-height:1.7}
.feature .hl{background:linear-gradient(transparent 55%,var(--yellow) 55%);font-weight:700}
.feature .accent{color:var(--pink-deep);font-weight:700}
.feature.col3{grid-column:3}
.opening-band{position:absolute;top:1046px;left:0;width:846px;height:44px;background:var(--pink);
  color:var(--white);font-family:"Zen Maru Gothic",sans-serif;font-weight:900;font-size:21px;
  line-height:44px;padding-left:20px;letter-spacing:1px}
.opening-band .big{font-size:28px;color:var(--yellow)}
.footer{position:absolute;top:1092px;left:0;width:846px;height:108px}
.company{position:absolute;left:20px;top:2px;font-size:11px;line-height:1.45}
.company .name{font-weight:800;font-size:15px}
.qr{position:absolute;left:300px;top:14px;width:76px;height:76px;background:#e9e3e5;border:3px solid var(--ink)}
.contact{position:absolute;left:390px;top:26px}
.contact .label{position:absolute;left:0;top:4px;width:44px;height:44px;border-radius:50%;background:var(--pink-deep);
  color:var(--white);font-size:11px;font-weight:700;text-align:center;line-height:1.2;padding-top:9px}
.contact .tel{display:block;margin-left:22px;padding:2px 14px 2px 30px;border:3px solid var(--pink);border-radius:30px;
  background:var(--white);color:var(--pink-deep);font-weight:800;font-size:28px;letter-spacing:1px}
.staff{position:absolute;left:636px;top:10px;width:196px;padding:8px 10px;border:2px solid var(--pink);
  background:var(--white);font-family:"Zen Maru Gothic",sans-serif;font-weight:700;
  font-size:14px;line-height:1.55;color:var(--pink-deep)}
.badge{position:absolute;right:14px;top:986px;width:92px;height:92px;border-radius:50%;background:var(--yellow);
  color:var(--pink-deep);font-weight:800;font-size:13px;text-align:center;line-height:1.35;padding-top:24px;transform:rotate(8deg)}
</style>
</head>
<body>
<div class="flyer">
  <header class="top-band">埼玉県で働いてみませんか?</header>
  <div class="hero-photo" role="img" aria-label="寄り添って手を重ねる介護スタッフと高齢者の写真"></div>
  <div class="wishes">
    <p>休日も充実させたい・・・。</p>
    <p>がんばりに応じた給与がほしい・・・。</p>
    <p>成長する機会がほしい・・・。</p>
  </div>
  <div class="invite">
    <span class="lead">そんなかたは、</span>
    <span class="main">こもれびで一緒に働きませんか?</span>
  </div>

  <section class="features">
    <article class="feature">
      <h2>給与は◎、物価も◎</h2>
      <p>みどり市は都心に比べて<span class="hl">家賃や物価が安く</span>、生活費を抑えられます。給与水準は都市部と変わらないため、<span class="accent">手元に残るお金が増えます。</span>貯金もしやすい環境です。</p>
    </article>
    <article class="feature">
      <h2>魅力的な給与体系</h2>
      <p>実績に応じて昇給する制度があり、<span class="hl">年収600万円以上も目指せます。</span>夜勤手当や資格手当も充実。入社1年目の賞与実績は<span class="accent">年2回・約4.0か月分</span>です。</p>
    </article>
    <article class="feature">
      <h2>都心へのアクセス良好</h2>
      <p>最寄り駅から電車で都心まで約60分。休日は<span class="hl">ショッピングや観光も気軽に</span>楽しめます。自然も多く、のびのびとした暮らしができます。</p>
    </article>
    <article class="feature">
      <h2>資格取得支援あり</h2>
      <p>介護福祉士などの<span class="hl">資格取得費用を法人が負担</span>します。研修制度も整っており、未経験からでも<span class="accent">安心してステップアップ</span>できます。</p>
    </article>
    <article class="feature col3">
      <h2>住宅支援</h2>
      <p>遠方からの入職者には<span class="hl">住宅手当を支給</span>します。借り上げ住宅の用意もあり、引っ越し費用も一部補助。<span class="accent">新生活を全力で応援します。</span></p>
    </article>
  </section>

  <div class="opening-band">令和5年6月に<span class="big">新施設開業予定!</span>積極的に採用を行っています!</div>
  <div class="badge">ご連絡<br>お待ちして<br>います!</div>

  <footer class="footer">
    <div class="company">
      <p class="name">株式会社LUMA</p>
      <p>埼玉県みどり市中央1-2-3</p>
      <p>住宅型有料老人ホームこもれび</p>
      <p>住宅型有料老人ホームこもれび2</p>
      <p>訪問介護事業所こもれび</p>
      <p>訪問看護ステーションこもれび</p>
    </div>
    <div class="qr" role="img" aria-label="施設ホームページのQRコード"></div>
    <div class="contact">
      <span class="label">問い<br>合わせ</span>
      <span class="tel">048-000-1234</span>
    </div>
    <div class="staff">詳しい話を聞きたい場合には、担当の森本、または早川まで。</div>
  </footer>
</div>
</body>
</html>
```